Radiant Harbor Holdings business card

We are a real estate advisory and investment company. We are specialized in assisting high networth individuals to invest in real estate overseas. We deliver a very personalized service, anticipating all the potential challenges an investor can face, and making it easy and safe for them. We also co-invest with our clients, assuring them that each project will be looked after as it is our own, and at the same time giving them the extra booth on confidence to invest.

We need a business card design. The business card must have a very premium, high-end look, reflecting principles like "commitment", "trust" and "timeless (but contemporary)". We look for long term relationships with our clients, and we grow with their referrals. We are all about conquering the confidence of the clients by always delivering above the expectations performance.

Target Market(s)

High net worth individuals.

Industry/Entity Type

Real Estate

Contact Information for Business Card

Please consider places on the business card for:

Name
Function (bellow name in smaller size text)

Mobile phone
E-mail
Skype ID
WeChat ID

Adress (3 lines)

Also include the following locations references:
PORTUGAL * DUBAI * HONG KONG

Website: www.rhholdings.example

Requirements
Must have
• Company Logo

```html
<!DOCTYPE html>
<html lang="en">
<head>
<meta charset="utf-8">
<title>Radiant Harbor Holdings — Business Card</title>
<link rel="stylesheet" href="https://fonts.googleapis.com/css2?family=Open+Sans:wght@400;600;700&display=swap">
<style>
  :root {
    --backdrop: #808184;
    --brand-blue: #29a9e1;
    --brand-grey: #77787b;
    --rule-grey: #8a8b8e;
    --paper: #ffffff;
    --ink: #6d6e71;
    --accent-green: #5cb531;
  }
  * { box-sizing: border-box; margin: 0; padding: 0; }
  html, body {
    width: 1200px; height: 828px; overflow: hidden;
    background: var(--backdrop);
    font-family: "Open Sans", Arial, sans-serif;
  }
  .sheet { position: relative; width: 1200px; height: 828px; }
  .card { position: absolute; width: 530px; height: 303px; overflow: hidden; }

  /* Front */
  .card--front { left: 337px; top: 64px; background: var(--paper); }
  .card--front .brand-name {
    position: absolute; left: 20px; top: 160px; width: 260px;
    text-align: center; white-space: nowrap; color: var(--brand-blue);
    font-weight: 600; font-size: 14px; letter-spacing: 1px; text-transform: uppercase;
  }
  .divider { position: absolute; left: 280px; top: 54px; width: 1px; height: 194px; background: #c4c5c7; }
  .contact { position: absolute; left: 295px; top: 53px; color: var(--ink); font-size: 13px; line-height: 18px; }
  .contact .person { color: var(--brand-blue); font-weight: 700; font-size: 13.5px; }
  .contact .role { margin-bottom: 8px; }
  .contact .address { margin-bottom: 8px; }
  .contact-line { display: flex; align-items: center; gap: 4px; height: 17.5px; }
  .contact-line svg { width: 13px; height: 13px; flex: none; }
  .band-rule { position: absolute; left: 0; bottom: 17px; width: 100%; height: 3px; background: var(--rule-grey); }
  .band { position: absolute; left: 0; bottom: 0; width: 100%; height: 15px; background: var(--brand-blue); }

  /* Backs */
  .card--back { top: 430px; }
  .card--blue { left: 50px; background: var(--brand-blue); }
  .card--grey { left: 631px; background: var(--brand-grey); }
  .card--back .brand-name {
    position: absolute; left: 0; top: 160px; width: 100%; text-align: center; white-space: nowrap;
    color: var(--paper); font-weight: 600; font-size: 23px; letter-spacing: 2px; text-transform: uppercase;
  }
  .locations {
    position: absolute; left: 0; top: 268px; width: 100%; text-align: center;
    color: var(--paper); font-size: 15.5px;
  }
</style>
</head>
<body>
<main class="sheet">
  <section class="card card--front" aria-label="Card front">
    <div class="brand-name">Radiant Harbor Holdings</div>
    <div class="divider"></div>
    <div class="contact">
      <div class="person">Daniel Mercer</div>
      <div class="role">President</div>
      <div class="address">N. 8 Alder Row,<br>Suite 240, Lakeview,<br>WA 50123</div>
      <div class="contact-line">
        <svg viewBox="0 0 13 13" aria-hidden="true"><rect width="13" height="13" rx="2" fill="#29a9e1"/><path d="M3.5 3h2l.7 2-1 .8a5 5 0 0 0 2 2l.8-1 2 .7v2c-4 .3-6.8-2.5-6.5-6.5z" fill="#fff"/></svg>
        555.010.274</div>
      <div class="contact-line">
        <svg viewBox="0 0 13 13" aria-hidden="true"><rect width="13" height="13" rx="2" fill="#29a9e1"/><rect x="2.5" y="3.5" width="8" height="6" fill="none" stroke="#fff"/><path d="M2.5 3.5l4 3.2 4-3.2" fill="none" stroke="#fff"/></svg>
        info@rhholdings.example</div>
      <div class="contact-line">
        <svg viewBox="0 0 13 13" aria-hidden="true"><rect width="13" height="13" rx="2" fill="#29a9e1"/><circle cx="6.5" cy="6.5" r="4" fill="none" stroke="#fff"/><path d="M2.5 6.5h8M6.5 2.5v8" stroke="#fff" stroke-width=".8"/></svg>
        www.rhholdings.example</div>
      <div class="contact-line">
        <svg viewBox="0 0 13 13" aria-hidden="true"><rect width="13" height="13" rx="2" fill="#29a9e1"/></svg>
        /rhHoldings</div>
      <div class="contact-line">
        <svg viewBox="0 0 13 13" aria-hidden="true"><rect width="13" height="13" rx="2" fill="#5cb531"/></svg>
        /rhHoldings</div>
    </div>
    <div class="band-rule"></div>
    <div class="band"></div>
  </section>

  <section class="card card--back card--blue" aria-label="Card back, blue">
    <div class="brand-name">Radiant Harbor Holdings</div>
    <div class="locations">Portugal • Dubai • Hong Kong</div>
  </section>

  <section class="card card--back card--grey" aria-label="Card back, grey">
    <div class="brand-name">Radiant Harbor Holdings</div>
    <div class="locations">Portugal • Dubai • Hong Kong</div>
  </section>
</main>
</body>
</html>
```